Simple and clean

We need a business card design for a new company called Estate Lantern. It is a search engine to find current properties for sale or rent in New Zealand market.
We have already a colour scheme that we would like people to use.
Light brown: #D4CCB0
Light green: #D6E4D4
Green: #669966
Black/White
It is OK to divert from this colour scheme slightly as long as there is a green component to the business card.
Final design should be clean, simple and should communicate the nature of the business.
Target Market(s)
- First home buyers
- Real estate agents
- People seeking rentals
Industry/Entity Type
Business
Requirements
Must have
- Use those or similar colours.
Light brown: #D4CCB0
Light green: #D6E4D4
Green: #669966
Black/White

```html
<!DOCTYPE html>
<html lang="en">
<head>
<meta charset="utf-8">
<title>Estate Lantern – Business Card</title>
<link rel="stylesheet" href="https://fonts.googleapis.com/css2?family=Open+Sans:wght@400;600;800&display=swap">
<style>
  :root {
    --page-bg: #ecebe6;
    --card-white: #ffffff;
    --ink: #1c1c1c;
    --green: #669966;
    --green-deep: #4f864f;
    --green-light: #d6e4d4;
    --band-grey: #cfd8cc;
    --brown-light: #d4ccb0;
    --text-dark: #222222;
  }
  * { box-sizing: border-box; margin: 0; padding: 0; }
  html, body { width: 1200px; height: 944px; overflow: hidden; }
  body {
    background: var(--page-bg);
    font-family: "Open Sans", Arial, sans-serif;
    position: relative;
  }
  .card {
    position: absolute;
    width: 700px;
    height: 400px;
    border-radius: 26px;
    background: linear-gradient(135deg, var(--card-white) 0%, #f3f3f1 100%);
    box-shadow: 0 10px 28px rgba(0,0,0,0.18);
    overflow: hidden;
  }
  .card-front { left: 110px; top: 60px; }
  .card-back { left: 390px; top: 484px; }

  .brand {
    position: absolute;
    left: 70px;
    top: 140px;
  }
  .brand-row {
    display: flex;
    align-items: center;
    gap: 20px;
  }
  .brand-square {
    width: 64px;
    height: 64px;
    background: var(--green);
  }
  .brand-name {
    font-weight: 800;
    font-size: 56px;
    color: var(--ink);
    letter-spacing: -1px;
    line-height: 1;
  }
  .brand-url {
    margin-top: 14px;
    margin-left: 84px;
    font-size: 27px;
    font-weight: 600;
    color: var(--green);
    letter-spacing: 0.5px;
  }

  .contact-band {
    position: absolute;
    left: 0;
    right: 0;
    top: 140px;
    height: 104px;
    display: flex;
  }
  .band-identity {
    width: 270px;
    background: linear-gradient(180deg, var(--green) 0%, var(--green-deep) 100%);
    color: #ffffff;
    padding: 28px 0 0 44px;
  }
  .person-name { font-size: 24px; font-weight: 400; line-height: 1.1; }
  .person-role { font-size: 16px; line-height: 1.3; }
  .band-details {
    flex: 1;
    background: linear-gradient(180deg, var(--green-light) 0%, var(--band-grey) 100%);
    border-left: 4px solid rgba(255,255,255,0.8);
    padding: 16px 0 0 22px;
    color: var(--text-dark);
    font-size: 18px;
    line-height: 1.3;
  }
</style>
</head>
<body>
  <section class="card card-front" aria-label="Business card front">
    <div class="brand">
      <div class="brand-row">
        <div class="brand-square"></div>
        <div class="brand-name">Estate Lantern</div>
      </div>
      <div class="brand-url">www.estatelantern.co.nz</div>
    </div>
  </section>

  <section class="card card-back" aria-label="Business card back">
    <div class="contact-band">
      <div class="band-identity">
        <div class="person-name">Mara Whitcombe</div>
        <div class="person-role">director</div>
      </div>
      <div class="band-details">
        <div class="detail-line">Phone&nbsp; 925-555-0140</div>
        <div class="detail-line">Cell&nbsp; 925-555-0141</div>
        <div class="detail-line">Email&nbsp; hello@estatelantern.co.nz</div>
      </div>
    </div>
  </section>
</body>
</html>
```